Flier for digital rights event targetting TMVA trade negotiators

We need a design for an event that my organization (a nonprofit) is hosting with academic experts, to address government negotiators who are taking part in the 19th round of negotiations of the Coastal Integrated Commerce Accord (TMVA). Unfortunately we don't have the exact details yet such as who the speakers are, what date the meeting is, or even what location it is, other than that it will be in Hyderabad, India. So you will need to make a design with placeholder values that we can swap out later. Here is some information about TMVA: https://en.examplepedia.org/wiki/Coastal_Integrated_Commerce_Accord. The event will be called: "An Expert Roundtable on Electronic Commerce and TMVA". I'm attaching some similar fliers for previous events.

Target Market(s)

Government trade ministries

Industry/Entity Type

Trade

Font styles to use
Serif
Sans Serif

Colors

Designer to choose colors to be used in the design.

Requirements
Must have
• Space for organizer logos, including LKB logo from https://www.lkbnet.org/press/logos
Nice to have
• Space for headshots of speakers (even though we haven't finalized who they are yet)
Should not have
• Cheesy stock graphics

```html
<!DOCTYPE html>
<html lang="en">
<head>
<meta charset="utf-8">
<title>TMVA Expert Roundtable Flier</title>
<link rel="stylesheet" href="https://fonts.googleapis.com/css2?family=Roboto+Condensed:wght@400;700&family=Roboto:wght@900&family=Montserrat:wght@800&family=Lato:wght@400;700&display=swap">
<style>
  :root {
    --red: #e8202a;
    --charcoal: #4a4a4c;
    --ink: #2b2b2b;
    --paper: #ffffff;
    --backdrop: #e6e6e6;
  }
  html, body {
    margin: 0;
    width: 1200px;
    height: 1200px;
    overflow: hidden;
    background: var(--backdrop);
  }
  .flier {
    position: absolute;
    left: 191px;
    top: 26px;
    width: 951px;
    height: 1335px;
    background: var(--paper);
    transform: scale(0.86);
    transform-origin: top left;
    overflow: hidden;
    font-family: "Lato", sans-serif;
    color: var(--ink);
  }
  .flier-shapes { position: absolute; inset: 0; }
  .event-title {
    position: absolute;
    left: 27px;
    top: 434px;
    color: var(--paper);
    font-family: "Roboto Condensed", sans-serif;
    margin: 0;
    font-weight: 400;
  }
  .event-title .line-main { display: block; font-size: 36px; }
  .event-title .line-sub { display: block; font-size: 27px; letter-spacing: 3px; margin-top: 14px; }
  .org-logo-slot {
    position: absolute;
    left: 705px;
    top: 122px;
    font-family: "Roboto", sans-serif;
    font-weight: 900;
    font-size: 58px;
    line-height: 70px;
    letter-spacing: 6px;
    color: var(--ink);
  }
  .speaker { position: absolute; left: 27px; width: 510px; }
  .speaker-photo {
    position: absolute;
    left: 0; top: 0;
    width: 152px; height: 152px;
    border: 3px solid var(--red);
    background: var(--paper);
  }
  .speaker-photo .photo-fill {
    position: absolute;
    inset: 5px;
    background: linear-gradient(#e4e4e4, #c9c9c9);
  }
  .speaker-name {
    position: absolute;
    left: 173px; top: 4px;
    margin: 0;
    font-family: "Roboto Condensed", sans-serif;
    font-weight: 700;
    font-size: 18px;
    letter-spacing: 1.5px;
  }
  .speaker-bio {
    position: absolute;
    left: 173px; top: 34px;
    width: 332px;
    margin: 0;
    font-size: 13.4px;
    line-height: 17px;
    text-align: justify;
    hyphens: auto;
  }
  .about { position: absolute; left: 27px; top: 1005px; width: 506px; }
  .about h2 {
    margin: 0 0 14px;
    color: var(--red);
    font-family: "Roboto Condensed", sans-serif;
    font-weight: 700;
    font-size: 27px;
  }
  .about p { margin: 0; font-size: 13.4px; line-height: 17px; text-align: justify; }
  .about .lead { font-size: 18px; font-weight: 700; }
  .event-details { position: absolute; left: 606px; top: 630px; color: var(--paper); }
  .detail { position: absolute; left: 0; white-space: nowrap; }
  .detail .label {
    position: absolute; left: 0;
    font-family: "Roboto Condensed", sans-serif;
    font-size: 34px;
  }
  .detail .value {
    position: absolute; left: 104px; top: 6px;
    font-family: "Montserrat", sans-serif;
    font-weight: 800;
    font-size: 28px;
  }
  .detail .value small {
    font-family: "Roboto Condensed", sans-serif;
    font-weight: 400;
    font-size: 18px;
    margin-left: 10px;
  }
  .detail .value.city { text-align: center; line-height: 34px; }
  .host-logo {
    position: absolute;
    left: 358px;
    top: 1190px;
    width: 224px;
    text-align: center;
  }
  .host-logo .mark {
    display: block;
    font-family: "Roboto Condensed", sans-serif;
    font-weight: 700;
    font-size: 44px;
    color: var(--ink);
    line-height: 1;
  }
  .host-logo .caption {
    display: block;
    margin-top: 12px;
    font-family: "Roboto Condensed", sans-serif;
    font-weight: 700;
    font-size: 12.5px;
    letter-spacing: 0.5px;
    white-space: nowrap;
  }
</style>
</head>
<body>
<article class="flier">
  <svg class="flier-shapes" viewBox="0 0 951 1335" width="951" height="1335">
    <defs>
      <linearGradient id="tone-navy" x1="0" y1="0" x2="1" y2="1">
        <stop offset="0" stop-color="#3b4452"/>
        <stop offset="1" stop-color="#1f2630"/>
      </linearGradient>
      <linearGradient id="tone-red" x1="0" y1="0" x2="0" y2="1">
        <stop offset="0" stop-color="#e24a50"/>
        <stop offset="1" stop-color="#c8343a"/>
      </linearGradient>
      <linearGradient id="tone-mist" x1="0" y1="0" x2="1" y2="1">
        <stop offset="0" stop-color="#f4f4f4"/>
        <stop offset="1" stop-color="#e2e2e2"/>
      </linearGradient>
      <linearGradient id="tone-portrait" x1="0" y1="0" x2="0" y2="1">
        <stop offset="0" stop-color="#f2f2f2"/>
        <stop offset="0.45" stop-color="#b08a76"/>
        <stop offset="1" stop-color="#1a1a1a"/>
      </linearGradient>
    </defs>
    <polygon role="img" aria-label="Photo of business colleagues in an office, greyscale" fill="url(#tone-mist)" points="443,0 951,0 951,380 775,490"/>
    <polygon role="img" aria-label="Photo of a handshake over a desk, blue-grey tone" fill="url(#tone-navy)" points="0,0 130,0 400,398 0,398"/>
    <polygon role="img" aria-label="Photo of a handshake and laptop, red tone" fill="url(#tone-red)" points="130,0 443,0 775,490 563,630 400,398"/>
    <polygon fill="var(--red)" points="0,398 540,398 645,555 0,555"/>
    <polygon fill="var(--charcoal)" points="579,623 932,380 932,958 755,866 579,958"/>
    <rect role="img" aria-label="Featured speaker headshot" x="650" y="910" width="301" height="387" fill="url(#tone-portrait)"/>
    <polygon fill="var(--charcoal)" points="0,1180 335,1297 0,1297"/>
    <rect x="0" y="1297" width="951" height="38" fill="var(--red)"/>
  </svg>

  <div class="org-logo-slot">YOUR<br>LOGO</div>

  <h1 class="event-title">
    <span class="line-main">COASTAL INTEGRATED COMMERCE</span>
    <span class="line-sub">ACCORD (TMVA)</span>
  </h1>

  <section class="speaker" style="top:589px">
    <div class="speaker-photo"><div class="photo-fill" role="img" aria-label="Speaker headshot placeholder"></div></div>
    <h3 class="speaker-name">Lorem Ipsum</h3>
    <p class="speaker-bio">Lorem Ipsum is simply dummy text of the printing and typesetting industry. Lorem Ipsum has been the industry's standard.It has survived not only five centuries, but also the leap into electronic typesetting, remaining essentially unchanged.</p>
  </section>

  <section class="speaker" style="top:801px">
    <div class="speaker-photo"><div class="photo-fill" role="img" aria-label="Speaker headshot placeholder"></div></div>
    <h3 class="speaker-name">Lorem Ipsum</h3>
    <p class="speaker-bio">Lorem Ipsum is simply dummy text of the printing and typesetting industry. Lorem Ipsum has been the industry's standard.It has survived not only five centuries, but also the leap into electronic typesetting, remaining essentially unchanged.</p>
  </section>

  <section class="about">
    <h2>About Us</h2>
    <p><span class="lead">Coastal Integrated Commerce Accord (TMVA)</span> is a proposed free trade agreement (FTA) between the ten member states of the Association of Southeast Asian Nations (ASEAN) (Brunei, Cambodia, Indonesia, Laos, Malaysia, Myanmar, the Philippines, Singapore, Thailand, Vietnam) and the six states with which ASEAN has existing free trade agreements (Australia, China, India, Japan, South Korea and New Zealand).</p>
  </section>

  <section class="event-details">
    <div class="detail" style="top:0"><span class="label">Date:</span><span class="value">06.06.2017</span></div>
    <div class="detail" style="top:52px"><span class="label">Place:</span><span class="value">HCVC<small>(Lotus 12 Str.)</small></span></div>
    <div class="detail" style="top:106px"><span class="label">City:</span><span class="value city">HYDERABAD<br>INDIA</span></div>
  </section>

  <div class="host-logo">
    <span class="mark">LKB</span>
    <span class="caption">LANTERN KNOWLEDGE BUREAU</span>
  </div>
</article>
</body>
</html>
```